LM Hair and Beauty flyer

Hello I have hairdressing salon called LM Hair and Beauty.I need flyer with double side pls.On front side I need this picture to be there and under the pisture our full address,tel number and email address( 48 Penwick rd E7 3QD 02084417396 media@lmhairandbeauty.co.uk). And under that shoud be written:Special offers
with 3 different discount squares at the bottom of the flyer.First visite 20% off,Second 15% off, thrd 10% off.At he other side of flyer should be following info:Ladies cut & blowdry with 3 different levels of stylist £45-£65,Gents cut £15-£36,Highlights from £45-£120,Express Blowdry £22-£35,Keratin tretmant £150,Manicure from £14,Pedicure from £25,Shellac from £28

Industry/Entity Type

Salon

```html
<!DOCTYPE html>
<html lang="en">
<head>
<meta charset="utf-8">
<title>LM Hair and Beauty – Flyer</title>
<link rel="stylesheet" href="https://fonts.googleapis.com/css2?family=Libre+Baskerville:wght@400;700&family=Source+Sans+3:wght@400;600;700&family=Oswald:wght@500;600&family=Open+Sans:wght@400;600&display=swap">
<style>
  :root {
    --page-bg: #e9e6e3;
    --plum-dark: #3a2130;
    --plum-deep: #3d2350;
    --taupe: #8a7468;
    --mauve: #8c7270;
    --gold: #c2ab86;
    --gold-light: #d8c6a3;
    --cream: #f3ece2;
    --text-grey: #5a4c55;
    --rule: #dcd6da;
    --photo-a: #cbbcb0;
    --photo-b: #6e5a55;
  }
  * { box-sizing: border-box; margin: 0; padding: 0; }
  html, body { width: 1200px; height: 1076px; overflow: hidden; }
  body { background: var(--page-bg); position: relative; font-family: "Source Sans 3", sans-serif; }

  .flyer { position: absolute; width: 545px; height: 780px; box-shadow: 0 6px 18px rgba(0,0,0,.25); overflow: hidden; }
  .flyer--front { left: 50px; top: 60px; background: var(--plum-dark); }
  .flyer--back { left: 610px; top: 250px; background: var(--mauve); }

  .brand-tag { position: absolute; left: 44px; top: 0; width: 72px; height: 72px; background: var(--plum-dark);
    display: flex; align-items: center; justify-content: center; text-align: center; padding: 6px;
    font-family: "Libre Baskerville", serif; font-size: 11px; line-height: 1.3; color: var(--cream); z-index: 2; }

  /* Front */
  .hero-photo { position: absolute; left: 0; top: 0; width: 545px; height: 590px;
    background: radial-gradient(ellipse at 50% 45%, var(--photo-a), var(--photo-b) 85%); }
  .quote { position: absolute; left: 0; right: 0; top: 362px; text-align: center; font-family: "Open Sans", sans-serif;
    font-size: 16px; font-weight: 600; color: #fff; text-shadow: 0 1px 3px rgba(0,0,0,.6); }
  .quote-author { position: absolute; right: 70px; top: 400px; font-family: "Open Sans", sans-serif; font-size: 10px; font-weight: 600; color: #fff; text-shadow: 0 1px 3px rgba(0,0,0,.6); }

  .contact-bar { position: absolute; left: 0; top: 590px; width: 545px; height: 44px; background: var(--taupe);
    display: flex; align-items: center; gap: 22px; padding-left: 22px; color: #fff; font-size: 13px; }
  .contact-bar .item { display: flex; align-items: center; gap: 6px; }
  .contact-bar svg { fill: var(--gold-light); }

  .offers-title { position: absolute; left: 22px; top: 648px; width: 170px; text-align: center; color: #fff; }
  .offers-title svg { stroke: var(--gold); }
  .offers-title h2 { font-family: "Libre Baskerville", serif; font-weight: 400; font-size: 27px; line-height: 1.05; letter-spacing: 1px; margin-top: 2px; }
  .offers-title .site { font-family: "Libre Baskerville", serif; font-size: 10px; color: var(--gold); margin-top: 4px; }

  .discounts { position: absolute; left: 200px; top: 648px; display: flex; gap: 9px; }
  .discount { width: 106px; height: 104px; border: 1px dashed var(--gold); padding: 9px; }
  .discount-inner { width: 100%; height: 100%; background: var(--gold); position: relative; text-align: center;
    font-family: "Oswald", sans-serif; color: var(--plum-dark); }
  .discount-label { font-size: 15px; line-height: .95; font-weight: 600; padding-top: 4px; }
  .discount-value { position: absolute; left: 4px; bottom: 2px; font-size: 38px; font-weight: 600; color: #fff; line-height: 1; letter-spacing: -1px; }
  .discount-value small { font-size: 26px; }
  .discount-off { position: absolute; right: 2px; bottom: 4px; writing-mode: vertical-rl; transform: rotate(180deg); font-size: 14px; color: #fff; }

  /* Back */
  .storefront { position: absolute; left: 0; top: 0; }
  .side-heading { position: absolute; left: 24px; top: 690px; transform: rotate(-90deg); transform-origin: left top;
    font-family: "Libre Baskerville", serif; font-size: 20px; letter-spacing: 2px; color: #a78f8b; white-space: nowrap; }
  .crown { position: absolute; left: 256px; top: 400px; }
  .price-card { position: absolute; left: 66px; top: 444px; width: 430px; background: #fff; padding: 7px 14px 7px 12px; }
  .price-row { display: flex; justify-content: space-between; align-items: center; min-height: 29px;
    border-bottom: 1px solid var(--rule); color: var(--text-grey); font-size: 13.5px; line-height: 1.15; }
  .price-row:first-child { min-height: 44px; }
  .price-row:last-child { border-bottom: none; }
  .price { background: var(--plum-deep); color: #fff; width: 166px; height: 23px; display: flex; align-items: center; justify-content: flex-end; padding-right: 6px; font-size: 13.5px; }

  .back-contacts { position: absolute; left: 0; right: 0; top: 736px; display: flex; justify-content: center; gap: 24px; color: #fff; font-size: 12.5px; }
  .back-contacts .item { display: flex; align-items: center; gap: 6px; }
  .back-contacts svg { fill: var(--gold-light); }
  .back-site { position: absolute; left: 0; right: 0; top: 756px; text-align: center; font-family: "Libre Baskerville", serif; font-size: 13px; color: var(--gold-light); }
</style>
</head>
<body>

<section class="flyer flyer--front">
  <div class="hero-photo" role="img" aria-label="Sepia group photo of the salon team posing together inside the salon"></div>
  <div class="brand-tag">LM Hair and Beauty</div>
  <p class="quote">“Everything you can imagine is real”</p>
  <p class="quote-author">Marco Delvane</p>

  <div class="contact-bar">
    <span class="item"><svg width="22" height="22" viewBox="0 0 24 24"><path d="M3 3h18v18H3zM5 5v14h14V5zM8 9h8v2H8zm0 4h8v2H8z"/></svg>48 Penwick rd E7 3QD</span>
    <span class="item"><svg width="10" height="12" viewBox="0 0 24 24"><path d="M6 2l4 5-2 3c1 3 3 5 6 6l3-2 5 4-3 4C9 21 3 15 2 5z"/></svg>02084417396</span>
    <span class="item"><svg width="12" height="9" viewBox="0 0 24 18"><path d="M0 0h24v18H0zM2 2l10 8 10-8z"/></svg>media@lmhairandbeauty.co.uk</span>
  </div>

  <div class="offers-title">
    <svg width="34" height="32" viewBox="0 0 34 32" fill="none" stroke-width="2"><path d="M6 4l22 20M28 4L6 24"/><circle cx="6" cy="27" r="3"/><circle cx="28" cy="27" r="3"/></svg>
    <h2>SPECIAL<br>OFFERS</h2>
    <p class="site">www.lmhairandbeauty.co.uk</p>
  </div>

  <div class="discounts">
    <div class="discount"><div class="discount-inner"><p class="discount-label">FIRST<br>VISITE</p><p class="discount-value">20<small>%</small></p><span class="discount-off">OFF</span></div></div>
    <div class="discount"><div class="discount-inner"><p class="discount-label">SECOND<br>VISITE</p><p class="discount-value">15<small>%</small></p><span class="discount-off">OFF</span></div></div>
    <div class="discount"><div class="discount-inner"><p class="discount-label">THRD<br>VISITE</p><p class="discount-value">10<small>%</small></p><span class="discount-off">OFF</span></div></div>
  </div>
</section>

<section class="flyer flyer--back">
  <svg class="storefront" width="545" height="400" viewBox="0 0 545 400" role="img" aria-label="Evening photo of the salon shopfront with red balloons and a woman seated on a bench">
    <defs>
      <linearGradient id="shopGrad" x1="0" y1="0" x2="0" y2="1">
        <stop offset="0" stop-color="#5a4470"/>
        <stop offset=".55" stop-color="#8a7a8c"/>
        <stop offset="1" stop-color="#3e2a3e"/>
      </linearGradient>
    </defs>
    <path d="M0 0H545V390Q440 350 300 385Q150 395 0 340Z" fill="url(#shopGrad)"/>
  </svg>
  <div class="brand-tag">LM Hair and Beauty</div>

  <svg class="crown" width="36" height="34" viewBox="0 0 36 34" fill="none" stroke="#d4bfa0" stroke-width="2"><path d="M3 10l7 8 8-12 8 12 7-8-3 16H6z"/><path d="M6 30h24"/></svg>

  <p class="side-heading">PRICES &amp; PRODUCTS</p>

  <div class="price-card">
    <div class="price-row"><span>Ladies cut &amp; blowdry<br>with 3 different levels of stylist</span><span class="price">£45-£65</span></div>
    <div class="price-row"><span>Gents cut</span><span class="price">£15-£36</span></div>
    <div class="price-row"><span>Highlights</span><span class="price">from £45-£120</span></div>
    <div class="price-row"><span>Express Blowdry</span><span class="price">£22-£35</span></div>
    <div class="price-row"><span>Keratin tretmant</span><span class="price">£150</span></div>
    <div class="price-row"><span>Manicure</span><span class="price">from £14</span></div>
    <div class="price-row"><span>Pedicure</span><span class="price">from £25</span></div>
    <div class="price-row"><span>Shellac</span><span class="price">from £28</span></div>
  </div>

  <div class="back-contacts">
    <span class="item"><svg width="12" height="11" viewBox="0 0 24 22"><path d="M12 0l12 10h-3v12h-6v-7H9v7H3V10H0z"/></svg>48 Penwick rd E7 3QD</span>
    <span class="item"><svg width="10" height="12" viewBox="0 0 24 24"><path d="M6 2l4 5-2 3c1 3 3 5 6 6l3-2 5 4-3 4C9 21 3 15 2 5z"/></svg>02084417396</span>
    <span class="item"><svg width="12" height="9" viewBox="0 0 24 18"><path d="M0 0h24v18H0zM2 2l10 8 10-8z"/></svg>media@lmhairandbeauty.co.uk</span>
  </div>
  <p class="back-site">www.lmhairandbeauty.co.uk</p>
</section>

</body>
</html>
```